Cover Page for our 2021 Comprehensive Needs Assessment Report 3 ring binder

Create a cover for our 2021 Comprehensive Needs Assessment. This is a report full of survey and non survey data, used for decision making. Modern Colors. Logo is attached as well as 2020 cover for easy explanation. However we do not want the same cover as last year, it should have a new color scheme for this year and a new look with the same feel.

Target Market(s)

School Districts

```html
<!DOCTYPE html>
<html lang="en">
<head>
<meta charset="utf-8">
<title>Comprehensive Needs Assessment 2021 – Binder Cover</title>
<link href="https://fonts.googleapis.com/css2?family=Bebas+Neue&family=Montserrat:wght@400;600&display=swap" rel="stylesheet">
<style>
  :root{
    --backdrop:#717275;
    --paper:#ffffff;
    --lime:#9dc83b;
    --navy:#131b2b;
    --cream:#fdf4d6;
    --photo-a:#d9d4cc;
    --photo-b:#8a7f78;
    --ink:#1a1a1a;
  }
  html,body{margin:0;padding:0;width:1200px;height:1200px;overflow:hidden;background:var(--backdrop);}
  .binder-cover{display:block;width:1200px;height:1200px;}
  .display{font-family:"Bebas Neue",Impact,sans-serif;}
  .body-copy{font-family:"Montserrat",Arial,sans-serif;font-size:17px;fill:var(--ink);}
  .brand-name{font-family:"Montserrat",Arial,sans-serif;font-weight:600;font-size:17px;fill:var(--ink);}
  .address{font-family:"Montserrat",Arial,sans-serif;font-size:15px;fill:var(--ink);}
</style>
</head>
<body>
<svg class="binder-cover" viewBox="0 0 1500 1500" xmlns="http://www.w3.org/2000/svg">
  <defs>
    <linearGradient id="photoTone" x1="0" y1="0" x2="1" y2="1">
      <stop offset="0" stop-color="var(--photo-b)"/>
      <stop offset="0.45" stop-color="var(--photo-a)"/>
      <stop offset="1" stop-color="#c9c2b8"/>
    </linearGradient>
  </defs>

  <!-- sheet -->
  <rect class="sheet" x="56" y="330" width="1389" height="842" fill="var(--paper)"/>

  <!-- ===== back cover ===== -->
  <g class="back-cover">
    <path class="accent-lime" d="M620,330 L651,330 L651,605 L590,618 Q560,622 566,595 Z" fill="var(--lime)"/>
    <path class="accent-lime" d="M56,782 L190,742 L178,788 L56,818 Z" fill="var(--lime)"/>
    <path class="photo-frame" role="img" aria-label="Photo of hands working over a table covered in planning notes and sticky notes"
          d="M56,330 L598,330 L540,560 Q520,625 460,645 L56,772 Z"
          fill="url(#photoTone)" stroke="var(--navy)" stroke-width="6"/>

    <g class="body-copy">
      <text x="222" y="759">Lorem ipsum dolor sit amet, consectetuer</text>
      <text x="222" y="781">adipiscing elit, sed diam nonummy nibh euis-</text>
      <text x="222" y="802">mod tincidunt ut laoreet dolore magna ali-</text>
      <text x="222" y="824">quam erat volutpat. Ut wisi enim ad minim</text>
      <text x="222" y="845">veniam, quis nostrud exerci tation ullamcorp-</text>
      <text x="222" y="867">er suscipit lobortis nisl ut aliquip ex ea com-</text>
      <text x="222" y="889">modo consequat. Duis autem vel eum iriure</text>
      <text x="222" y="910">dolor in hendrerit in vulputate velit esse mo-</text>
      <text x="222" y="932">lestie consequat, vel illum dolore eu feugiat</text>
      <text x="222" y="953">nulla facilisis at vero eros et accumsan et</text>
    </g>

    <g class="brand back-brand">
      <circle cx="118" cy="1042" r="8" fill="var(--lime)"/>
      <text class="brand-name" x="132" y="1038">Learning</text>
      <text class="brand-name" x="132" y="1060">Pathways, LLC</text>
    </g>
    <g class="address" text-anchor="middle">
      <text x="187" y="1095">4512 Willow Bend Lane</text>
      <text x="187" y="1115">Fairmont, MS 38601</text>
      <text x="187" y="1134">662.555.0148</text>
    </g>

    <path class="accent-lime" d="M355,1090 L651,984 L651,1000 L370,1098 Z" fill="var(--lime)"/>
    <path class="base-navy" d="M285,1172 Q292,1110 360,1088 L651,994 L651,1172 Z" fill="var(--navy)"/>
  </g>

  <!-- ===== spine ===== -->
  <g class="spine">
    <rect x="651" y="330" width="199" height="470" fill="var(--lime)"/>
    <path class="base-navy" d="M651,798 L800,752 Q850,738 850,772 L850,1172 L651,1172 Z" fill="var(--navy)"/>

    <g class="brand spine-brand">
      <circle cx="697" cy="402" r="8" fill="var(--paper)"/>
      <text class="brand-name" x="710" y="398">Learning</text>
      <text class="brand-name" x="710" y="418">Pathways, LLC</text>
    </g>

    <text class="display" transform="translate(752,475) rotate(90)" font-size="54" fill="var(--navy)" textLength="253" lengthAdjust="spacingAndGlyphs">COMPREHENSIVE</text>
    <text class="display" transform="translate(714,475) rotate(90)" font-size="44" fill="var(--paper)" textLength="252" lengthAdjust="spacingAndGlyphs">NEEDS ASSESSMENT</text>
    <text class="display" transform="translate(748,836) rotate(90)" font-size="62" fill="var(--paper)" textLength="222" lengthAdjust="spacingAndGlyphs">HARLOW</text>
    <text class="display" transform="translate(713,836) rotate(90)" font-size="34" fill="var(--paper)" textLength="220" lengthAdjust="spacingAndGlyphs">SCHOOL DISTRICT</text>
  </g>

  <!-- ===== front cover ===== -->
  <g class="front-cover">
    <path class="accent-lime" d="M850,330 L1102,330 L1070,430 Q1058,458 1020,468 L850,512 Z" fill="var(--lime)"/>
    <path class="accent-cream" d="M850,330 L1075,330 L1048,418 Q1038,442 1005,450 L850,492 Z" fill="var(--cream)"/>

    <g class="brand front-brand">
      <circle cx="884" cy="402" r="8" fill="var(--lime)"/>
      <text class="brand-name" x="897" y="398">Learning</text>
      <text class="brand-name" x="897" y="418">Pathways, LLC</text>
    </g>

    <path class="accent-lime" d="M1445,515 L1445,800 L1372,805 Q1350,802 1358,772 L1428,528 Z" fill="var(--lime)"/>
    <path class="accent-lime" d="M850,895 L992,855 L968,958 L850,998 Z" fill="var(--lime)"/>

    <path class="photo-frame" role="img" aria-label="Photo of hands working over a table covered in planning notes and sticky notes"
          d="M850,498 L1372,350 Q1412,340 1405,382 L1330,705 Q1314,762 1252,780 L850,900 Z"
          fill="url(#photoTone)" stroke="var(--navy)" stroke-width="6"/>

    <text class="display title-main" x="1013" y="930" font-size="86" fill="var(--navy)" textLength="387" lengthAdjust="spacingAndGlyphs">COMPREHENSIVE</text>
    <text class="display title-sub" x="1013" y="994" font-size="72" fill="var(--lime)" textLength="387" lengthAdjust="spacingAndGlyphs">NEEDS ASSESSMENT</text>

    <text class="display district-name" x="903" y="1088" font-size="56" fill="var(--navy)" textLength="190" lengthAdjust="spacing">HARLOW</text>
    <text class="display district-label" x="900" y="1120" font-size="34" fill="var(--lime)" textLength="203" lengthAdjust="spacing">SCHOOL DISTRICT</text>

    <path class="accent-lime" d="M1185,1085 L1445,996 L1445,1012 L1200,1094 Z" fill="var(--lime)"/>
    <path class="base-navy" d="M1115,1172 Q1120,1110 1190,1088 L1445,1008 L1445,1172 Z" fill="var(--navy)"/>
    <text class="display report-year" x="1243" y="1139" font-size="82" fill="var(--paper)" textLength="154" lengthAdjust="spacing">2021</text>
  </g>
</svg>
</body>
</html>
```